Vireo Halden Business Cards

Vireo Halden Luxury Brand Collection is a global representation business focusing on high end luxury. We need business cards to epitomize our global, luxury delivery model.

Target Market(s)

Global Representation in the hospitality industry

Industry/Entity Type

Hospitality

Contact Information for Business Card

name
title
email: first.last@vh-kmt.com
web: www.vh-kmt.com
mobile:

Requirements
Must have
• double sided design
• incorporate logo colours
• have logo prominent
Should not have
• no designs not incorporating logo colours.

```html
<!DOCTYPE html>
<html lang="en">
<head>
<meta charset="utf-8">
<title>Vireo Halden Business Cards</title>
<link href="https://fonts.googleapis.com/css2?family=Cinzel:wght@600&family=Arimo&display=swap" rel="stylesheet">
<style>
  :root {
    --backdrop: #1f1f1f;
    --gold: #826d3f;
    --gold-deep: #6a5532;
    --paper: #ffffff;
    --ghost: rgba(205, 196, 178, 0.22);
    --ink-light: #ffffff;
  }
  html, body {
    margin: 0;
    padding: 0;
    width: 1200px;
    height: 1200px;
    overflow: hidden;
    background: var(--backdrop);
  }
  .canvas {
    position: relative;
    width: 1200px;
    height: 1200px;
  }
  .card {
    position: absolute;
    overflow: hidden;
    box-shadow: 8px 10px 18px rgba(0, 0, 0, 0.55);
  }
  .card-front {
    left: 290px;
    top: 194px;
    width: 678px;
    height: 368px;
    background: linear-gradient(180deg, var(--gold) 0%, var(--gold) 40%, var(--gold-deep) 100%);
  }
  .card-back {
    left: 288px;
    top: 632px;
    width: 674px;
    height: 368px;
    background: linear-gradient(90deg, var(--gold) 0, var(--gold) 338px, var(--paper) 338px);
  }
  .brand-name {
    font-family: "Cinzel", "Times New Roman", serif;
    font-weight: 600;
    letter-spacing: 0.04em;
    white-space: nowrap;
    position: absolute;
    margin: 0;
  }
  .front-brand {
    color: var(--ink-light);
    font-size: 42px;
    left: 0;
    right: 0;
    top: 160px;
    text-align: center;
  }
  .ghost-brand {
    color: var(--ghost);
    font-size: 58px;
    line-height: 1.05;
    left: 200px;
    width: 300px;
    top: 108px;
    text-align: center;
    white-space: normal;
  }
  .back-brand {
    color: var(--gold);
    font-size: 21px;
    left: 500px;
    width: 140px;
    top: 275px;
    text-align: center;
  }
  .contact {
    position: absolute;
    left: 41px;
    top: 160px;
    margin: 0;
    font-family: "Arimo", Arial, sans-serif;
    font-size: 23px;
    line-height: 30px;
    color: var(--ink-light);
    font-style: normal;
  }
</style>
</head>
<body>
<main class="canvas">
  <section class="card card-front" aria-label="Business card front">
    <p class="brand-name front-brand">Vireo Halden</p>
  </section>

  <section class="card card-back" aria-label="Business card back">
    <p class="brand-name ghost-brand" aria-hidden="true">Vireo Halden</p>
    <address class="contact">
      first.last@vh-kmt.com<br>
      www.vh-kmt.com
    </address>
    <p class="brand-name back-brand">Vireo Halden</p>
  </section>
</main>
</body>
</html>
```